Association qui souhaite améliorer l'accès aux personnes en situation de handicap

Nous sommes une association qui a pour objectif d'améliorer l'accessibilité, augmenter l'offre des activités réalisables dans notre région touristique.
Nous souhaitons réaliser un site internet afin de pouvoir communiquer sur notre association. Nous avons déjà conçu notre flyer sur Graphivolta. Nous souhaiterions une base graphique se rapportant à celui-ci. C'est possible de tout retravailler mais nous souhaitons tout de même retrouver la charte graphique ou code couleur du flyer.
Il nous faudrait quelques pages:
- 1 page : Acceuil / Présentation (Home), Il y aurait le descriptif de l'association, avec ses objectifs à +/- moyen terme
- 1 page : Nos réalisations, celle-ci présenterait les éléments que nous avons réalisés avec des zones de textes et des images classées chronologiquement au fur et à mesure des nouveautés
- 1 page : Media, comme la précédente, mais ou on pourrait voir ou lire sur les divers médias qui parlent de nous
- 1 page : Evenements : c'est une page pour présenter divers activités que nous allons organiser
- 1 page : Contact qui indique comment nous contacter et avec la présentation des 5 ou 6 membres du comité
- 1 link donate : qui arrive sur un formulaire de donnée que l'on pourra faire évoluer sur un système de payement par la suite. Cette bannière doit se retrouver sur toutes les pages
Il est nécessaire que se design puisse être transféré sur une lecture sur téléphone mobile
Target Market(s)
Personnes en situation de handicap
Industry/Entity Type
Associatif
Coding
Coded - Design and coding required
Number of Pages Required
5+ page

```html
<!DOCTYPE html>
<html lang="en">
<head>
<meta charset="utf-8">
<title>Openway Association – Our Achievements</title>
<link href="https://fonts.googleapis.com/css2?family=Raleway:wght@500;800&family=Mulish:wght@400;600;700&family=Oswald:wght@500&display=swap" rel="stylesheet">
<style>
  :root {
    --red: #be1a28;
    --ink: #1c1c1c;
    --text: #222;
    --footer: #262d30;
    --footer-text: #e8eaeb;
    --white: #fff;
  }
  * { margin: 0; padding: 0; box-sizing: border-box; }
  html, body { width: 801px; height: 1200px; overflow: hidden; background: var(--white); }
  body { position: relative; font-family: "Mulish", sans-serif; color: var(--text); }
  .abs { position: absolute; }

  .topbar { left: 0; top: 0; width: 801px; height: 19px; background: var(--red); }
  .topbar .social-dot { left: 86px; top: 5px; width: 8px; height: 8px; border-radius: 50%; background: var(--white); }
  .topbar .mail { right: 86px; top: 4px; font-size: 7px; color: var(--white); display: flex; align-items: center; gap: 3px; }

  .header { left: 0; top: 19px; width: 801px; height: 41px; background: var(--white); }
  .brand { left: 87px; top: 12px; display: flex; align-items: center; gap: 5px; font-family: "Mulish", sans-serif; font-weight: 700; font-size: 9px; color: var(--red); letter-spacing: .2px; }
  .brand .mark { width: 9px; height: 9px; background: var(--red); }
  .nav { top: 14px; font-size: 7.3px; color: var(--ink); }
  .nav.active { color: var(--red); }
  .nav-zigzag { left: 431px; top: 25px; }
  .donate { left: 652px; top: 11px; width: 62px; height: 20px; border-radius: 10px; background: var(--red); color: var(--white); font-size: 7px; font-weight: 700; display: flex; align-items: center; justify-content: center; }

  .hero { left: 0; top: 60px; width: 801px; height: 182px;
    background: radial-gradient(ellipse at 55% 60%, #5a5040 0%, #2e2a22 45%, #15170f 100%); }
  .hero-title { left: 0; width: 801px; top: 128px; text-align: center; font-family: "Raleway", sans-serif; font-weight: 800; font-size: 23px; color: var(--white); }
  .hero-title span { color: #e0202f; }
  .crumb { left: 0; width: 801px; top: 161px; text-align: center; font-size: 6.5px; color: #ddd; }
  .crumb b { font-weight: 400; color: var(--white); }

  .shapes { left: 0; top: 0; }

  h2.section-title { font-family: "Raleway", sans-serif; font-weight: 500; font-size: 22.5px; color: var(--ink); line-height: 1.3; }
  .body-copy { font-size: 8.6px; line-height: 12.9px; color: var(--text); }

  .footer-text { font-size: 7px; color: var(--footer-text); }
  .footer-head { font-family: "Oswald", sans-serif; font-weight: 500; font-size: 10.5px; color: #e0202f; letter-spacing: .2px; }
  .footer-list { list-style: none; font-size: 7px; line-height: 15.2px; color: var(--footer-text); }
  .f-brand { left: 87px; top: 1010px; display: flex; align-items: center; gap: 5px; font-weight: 700; font-size: 10px; color: var(--white); }
  .f-brand .mark { width: 10px; height: 10px; background: var(--white); }
  .f-social { left: 87px; top: 1093px; width: 15px; height: 15px; border-radius: 50%; background: var(--red); }
  .contact-row { display: flex; gap: 5px; align-items: flex-start; }
  .contact-icon { width: 15px; height: 15px; border: 1px solid #9aa0a3; border-radius: 50%; flex: none; display: flex; align-items: center; justify-content: center; }
  .rule { left: 87px; top: 1139px; width: 627px; border-top: 1px dotted #4a5256; }
  .copyright { left: 0; width: 801px; top: 1155px; text-align: center; font-size: 7px; color: var(--footer-text); }
  .copyright span { color: #e0202f; }
</style>
</head>
<body>

  <div class="abs topbar">
    <div class="abs social-dot"></div>
    <div class="abs mail">
      <svg width="8" height="6" viewBox="0 0 8 6"><rect width="8" height="6" fill="#fff"/><path d="M0 0 L4 3.5 L8 0" stroke="#be1a28" stroke-width=".8" fill="none"/></svg>
      info@openway-association.org
    </div>
  </div>

  <header class="abs header">
    <div class="abs brand"><span class="mark"></span>OPENWAY ASSOCIATION</div>
    <span class="abs nav" style="left:360px">Home</span>
    <span class="abs nav active" style="left:407px">Our Achievements</span>
    <svg class="abs nav-zigzag" width="21" height="6" viewBox="0 0 21 6"><path d="M0 1 L4 5 L8 1 L12 5 L16 1 L20 5" stroke="#be1a28" stroke-width="1" fill="none"/></svg>
    <span class="abs nav" style="left:496px">Media</span>
    <span class="abs nav" style="left:543px">Events</span>
    <span class="abs nav" style="left:592px">Contacts</span>
    <div class="abs donate">DONATE</div>
  </header>

  <section class="abs hero" role="img" aria-label="Photo of two women laughing in a forest, one seated in a wheelchair"></section>
  <h1 class="abs hero-title">OUR <span>ACHIEVEMENTS</span></h1>
  <div class="abs crumb">Home | <b>Achivements</b></div>

  <svg class="abs shapes" width="801" height="1200" viewBox="0 0 801 1200">
    <defs>
      <linearGradient id="meadow" x1="0" y1="0" x2="1" y2="1">
        <stop offset="0" stop-color="#f3f0e6"/>
        <stop offset=".45" stop-color="#a6b27a"/>
        <stop offset="1" stop-color="#3f5a2c"/>
      </linearGradient>
      <linearGradient id="child" x1="0" y1="0" x2="1" y2="1">
        <stop offset="0" stop-color="#e9c8bc"/>
        <stop offset=".45" stop-color="#4f8a3a"/>
        <stop offset="1" stop-color="#2b2e8a"/>
      </linearGradient>
    </defs>
    <polygon points="420,242 801,242 801,427 626,576" fill="url(#meadow)" role="img" aria-label="Photo of an older person in a wheelchair touching tall grass in a sunny meadow"/>
    <polygon points="245,242 695,508 626,570" fill="#be1a28" opacity=".88"/>
    <polygon points="801,432 801,478 630,580" fill="#be1a28"/>
    <polygon points="307,633 354,913 88,815" fill="#be1a28"/>
    <polygon points="290,626 363,900 88,827" fill="url(#child)" role="img" aria-label="Photo of a young girl blowing on a dandelion in a green field"/>
    <polygon points="0,929 315,977 801,893 801,1200 0,1200" fill="#262d30"/>
  </svg>

  <h2 class="abs section-title" style="left:86px; top:323px">Our Achievements</h2>
  <p class="abs body-copy" style="left:87px; top:369px; width:272px">Sed ut perspiciatis unde omnis iste natus error sit voluptatem accusantium doloremque laudantium, totam rem aperiam, eaque ipsa quae ab illo inventore veritatis et quasi architecto beatae vitae dicta sunt explicabo. Nemo enim ipsam voluptatem quia voluptas sit aspernatur aut odit aut fugit, sed quia consequuntur magni dolores eos qui ratione voluptatem sequi nesciunt. Neque porro quisquam est, qui dolorem ipsum quia dolor sit amet, consectetur, adipisci velit, sed quia non numquam eius modi tempora incidunt ut labore et dolore magnam aliquam quaerat voluptatem.</p>
  <p class="abs body-copy" style="left:87px; top:508px; width:446px">But I must explain to you how all this mistaken idea of denouncing pleasure and praising pain was born and I will give you a complete account of the system, and expound the actual teachings of the great explorer of the truth, the master-builder of human happiness. No one rejects, dislikes</p>

  <h2 class="abs section-title" style="left:406px; top:692px; width:320px">These Cases are Perfectly Distinguish</h2>
  <p class="abs body-copy" style="left:407px; top:765px; width:308px">Sed ut perspiciatis unde omnis iste natus error sit voluptatem accusantium doloremque laudantium, totam rem aperiam, eaque ipsa quae ab illo inventore veritatis et quasi architecto beatae vitae dicta sunt explicabo. Nemo enim ipsam voluptatem quia voluptas sit aspernatur aut odit aut fugit, sed quia consequuntur magni dolores...</p>

  <footer>
    <div class="abs f-brand"><span class="mark"></span>OPENWAY ASSOCIATION</div>
    <p class="abs footer-text" style="left:87px; top:1048px; width:138px; line-height:10.8px">Sed ut perspiciatis unde omnis iste natus error sit voluptatem accusantium rem aperiam</p>
    <div class="abs f-social"></div>

    <div class="abs" style="left:300px; top:1000px">
      <div class="footer-head">SITEMAP</div>
      <ul class="footer-list" style="margin-top:4px">
        <li>Home</li><li>Our Achivements</li><li>Media</li><li>Events</li><li>Contact Us</li>
      </ul>
    </div>
    <div class="abs" style="left:447px; top:1000px">
      <div class="footer-head">OTHERS</div>
      <ul class="footer-list" style="margin-top:4px">
        <li>Privacy Policy</li><li>Terms &amp; Conditions</li><li>Leagal</li><li>Donate</li><li>Help / Support</li>
      </ul>
    </div>
    <div class="abs" style="left:584px; top:1000px">
      <div class="footer-head">CONTACTS</div>
      <div class="contact-row footer-text" style="margin-top:7px; line-height:9.5px">
        <span class="contact-icon"><svg width="6" height="8" viewBox="0 0 6 8"><path d="M3 8 C1 5 0 4 0 3 A3 3 0 0 1 6 3 C6 4 5 5 3 8Z" fill="#be1a28"/><circle cx="3" cy="3" r="1" fill="#262d30"/></svg></span>
        <span>Chemin du Vallon 8 / 1999<br>Valdorre</span>
      </div>
      <div class="contact-row footer-text" style="margin-top:9px; align-items:center">
        <span class="contact-icon"><svg width="8" height="6" viewBox="0 0 8 6"><rect width="8" height="6" fill="#be1a28"/><path d="M0 0 L4 3.5 L8 0" stroke="#262d30" stroke-width=".8" fill="none"/></svg></span>
        <span>info@openway-association.org</span>
      </div>
    </div>

    <div class="abs rule"></div>
    <p class="abs copyright">Copyright © 2022 <span>Openway Association</span>. All Rights Reserved.</p>
  </footer>

</body>
</html>
```